Tilda Tinkerwire, An IT Company Has New Logo, Need Fresh Business Cards

IT company is called Tilda Tinkerwire and is displayed nicely with the new logo from here on pitchloft. Would like a fresh business card look that encompasses the idea that we want clients to Cherish Every Gadget. I love the use of circuitry with hearts as endpoints and x's and o's. It needs to have room for my certification logos of which there are 4 and a BRJ Alumni log. I am attaching my current card to illustrate how it has always captured attention, but that was in the early stages of business when I was doing more residential work. I am focused on businesses now, so a level of professionalism is necessary. I would also like the card to lend itself well to additional stationary, email signature, ticketing template for my workboard, etc. For the time being, I need the card for an upcoming conference so that work will come later. Color scheme should be that of the new logo. Thank you and I look forward to the designs.

Target Market(s)

Businesses looking for IT services.

Industry/Entity Type

Information Technology

Contact Information for Business Card

See above

Requirements
Must have
• New logo colors and a warm feel. Possibly a tad feminine as I am female, but appealing to males.
Nice to have
• I would like techy, but no too much so. I like friendly and connecting feels. People LOVED my old card and called me because it gave them a warm feeling.

```html
<!DOCTYPE html>
<html lang="en">
<head>
<meta charset="utf-8">
<title>Tilda Tinkerwire – Business Cards</title>
<link rel="stylesheet" href="https://fonts.googleapis.com/css2?family=Source+Sans+3:ital,wght@0,400;0,600;0,700;1,600;1,700&display=swap">
<style>
  :root {
    --backdrop: #7b7b7b;
    --card: #0b0b0b;
    --band: #f4f4f4;
    --sky: #8fd0ec;
    --lime: #d6e888;
    --rose: #c98aa6;
    --white: #ffffff;
    --ink: #1c1c1c;
    --badge: #c9d3dc;
    --badge-accent: #9ac0de;
  }
  * { box-sizing: border-box; margin: 0; padding: 0; }
  html, body { width: 1200px; height: 1191px; overflow: hidden; }
  body {
    background: var(--backdrop);
    font-family: "Source Sans 3", "Myriad Pro", Arial, sans-serif;
    position: relative;
  }
  .card {
    position: absolute;
    left: 234px;
    width: 732px;
    height: 417px;
    background: var(--card);
    overflow: hidden;
  }
  .card--front { top: 133px; }
  .card--back { top: 640px; }

  .brand {
    position: absolute;
    left: 0; right: 0;
    text-align: center;
  }
  .brand__mark {
    display: block;
    margin: 0 auto 14px;
    width: 112px; height: 112px;
    border-radius: 50%;
    background: radial-gradient(circle, #2a2a2a 0%, #141414 100%);
    border: 2px solid #2e2e2e;
  }
  .brand__name {
    font-size: 32px;
    font-weight: 600;
    color: var(--sky);
    letter-spacing: 0.2px;
    line-height: 1;
  }
  .brand__tagline {
    margin-top: 6px;
    font-size: 11px;
    letter-spacing: 3px;
    text-transform: uppercase;
    color: var(--lime);
  }
  .card--front .brand { top: 28px; }
  .card--back .brand { top: 34px; }

  .contact-name {
    position: absolute;
    top: 26px; left: 34px;
    display: flex; align-items: center; gap: 12px;
    font-size: 31px; font-weight: 700; color: var(--sky);
  }
  .contact-phone {
    position: absolute;
    top: 34px; right: 36px;
    display: flex; align-items: center; gap: 6px;
    font-size: 23px; font-weight: 600; font-style: italic; color: var(--lime);
  }
  .icon { fill: var(--sky); }

  .cert-band {
    position: absolute;
    left: 0; right: 0;
    height: 86px;
    background: var(--band);
    display: flex; align-items: center;
    padding: 0 32px 0 40px;
    gap: 22px;
  }
  .card--front .cert-band { top: 223px; }
  .card--back .cert-band { top: 320px; height: 80px; }
  .cert-badge {
    width: 94px; height: 44px;
    border-radius: 3px;
    background: linear-gradient(180deg, var(--badge) 0 50%, var(--badge-accent) 50% 100%);
  }
  .cert-badge--wide { width: 140px; }
  .alumni {
    margin-left: auto;
    display: flex; align-items: center; gap: 12px;
    color: var(--ink);
  }
  .alumni__school {
    display: flex; flex-direction: column; align-items: center;
    font-size: 15px; font-weight: 700;
  }
  .alumni__dot {
    width: 26px; height: 26px; border-radius: 50%;
    background: #e9b200; margin-bottom: 3px;
  }
  .alumni__rule { width: 2px; height: 50px; background: var(--ink); }
  .alumni__label { font-size: 25px; font-weight: 600; }

  .web-line {
    position: absolute;
    left: 0; right: 0;
    text-align: center;
    font-size: 22px;
    color: var(--white);
  }
  .card--front .web-line { top: 318px; }
  .card--back .web-line { top: 270px; }
  .services {
    position: absolute;
    top: 357px; left: 0; right: 0;
    text-align: center;
    font-size: 24px; font-weight: 600; font-style: italic;
    color: var(--lime);
  }
  .call-line {
    position: absolute;
    top: 224px; left: 0; right: 0;
    text-align: center;
    font-size: 32px; font-weight: 700;
    color: var(--sky);
  }
  .call-line__verb { color: var(--rose); font-style: italic; }
  .call-line__phone { font-size: 23px; font-style: italic; font-weight: 600; color: var(--lime); }
</style>
</head>
<body>

<section class="card card--front">
  <div class="contact-name">
    <svg class="icon" width="18" height="20" viewBox="0 0 18 20" aria-hidden="true"><circle cx="9" cy="5.5" r="5"/><path d="M0 20c0-6 4-8.5 9-8.5s9 2.5 9 8.5z"/></svg>
    Tilda
  </div>
  <div class="contact-phone">
    <svg class="icon" width="18" height="18" viewBox="0 0 24 24" aria-hidden="true"><path d="M6.6 10.8a15 15 0 0 0 6.6 6.6l2.2-2.2c.3-.3.7-.4 1-.2 1.1.4 2.3.6 3.6.6.6 0 1 .4 1 1V20c0 .6-.4 1-1 1A17 17 0 0 1 3 4c0-.6.4-1 1-1h3.5c.6 0 1 .4 1 1 0 1.3.2 2.5.6 3.6.1.3 0 .7-.2 1z"/></svg>
    407-555-0148
  </div>
  <div class="brand">
    <span class="brand__mark" role="img" aria-label="Tilda Tinkerwire logo symbol area"></span>
    <div class="brand__name">Tilda Tinkerwire</div>
    <div class="brand__tagline">Cherish Every Gadget</div>
  </div>
  <div class="cert-band">
    <span class="cert-badge" role="img" aria-label="Certification badge"></span>
    <span class="cert-badge" role="img" aria-label="Certification badge"></span>
    <span class="cert-badge" role="img" aria-label="Certification badge"></span>
    <span class="cert-badge cert-badge--wide" role="img" aria-label="Certification badge"></span>
    <div class="alumni">
      <div class="alumni__school"><span class="alumni__dot"></span>BRJ</div>
      <span class="alumni__rule"></span>
      <span class="alumni__label">Alumni</span>
    </div>
  </div>
  <p class="web-line">tilda.tinkerwire@mailnest.com | tilda-tinkerwire.com</p>
  <p class="services">Desktops - Laptops - Tablets&nbsp; Service, Care &amp; Repaire</p>
</section>

<section class="card card--back">
  <div class="brand">
    <span class="brand__mark" role="img" aria-label="Tilda Tinkerwire logo symbol area"></span>
    <div class="brand__name">Tilda Tinkerwire</div>
    <div class="brand__tagline">Cherish Every Gadget</div>
  </div>
  <p class="call-line"><span class="call-line__verb">Call</span> Tilda - <span class="call-line__phone">407-555-0148</span></p>
  <p class="web-line">tilda.tinkerwire@mailnest.com | tilda-tinkerwire.com</p>
  <div class="cert-band">
    <span class="cert-badge" role="img" aria-label="Certification badge"></span>
    <span class="cert-badge" role="img" aria-label="Certification badge"></span>
    <span class="cert-badge" role="img" aria-label="Certification badge"></span>
    <span class="cert-badge cert-badge--wide" role="img" aria-label="Certification badge"></span>
    <div class="alumni">
      <div class="alumni__school"><span class="alumni__dot"></span>BRJ</div>
      <span class="alumni__rule"></span>
      <span class="alumni__label">Alumni</span>
    </div>
  </div>
</section>

</body>
</html>
```